Varneck Bidding Business Cards Design Needed

I need a business card design that is modern looking - double sided (maybe just my logo on the back, but open to suggestions) - the overall design is up to you. I want it to be easy to read - not over the top flashy. I already have a company logo which I uploaded so that needs to be used. The colors of my logo are the colors I want on the card... so blue and gray (do need to match the logo colors).

Requirements
Must have
• Would like the card to be sleek, modern and easy to ready

```html
<!DOCTYPE html>
<html lang="en">
<head>
<meta charset="utf-8">
<title>Varneck Bidding – Business Cards</title>
<link rel="stylesheet" href="https://fonts.googleapis.com/css2?family=Exo+2:wght@600;700&family=Roboto:wght@400;500;700&display=swap">
<style>
  :root {
    --brand-blue: #2f7fc4;
    --back-blue: #2b78ba;
    --brand-gray: #5e5e60;
    --text-gray: #555557;
    --divider: #d4d4d4;
    --paper: #ffffff;
    --backdrop: #1e1e1f;
  }
  * { margin: 0; padding: 0; box-sizing: border-box; }
  html, body {
    width: 1125px; height: 1200px; overflow: hidden;
    background: var(--backdrop);
  }
  .canvas { position: relative; width: 1125px; height: 1200px; }

  .card {
    position: absolute; left: 150px; width: 825px; height: 471px; overflow: hidden;
  }
  .card--front { top: 98px; background: var(--paper); }
  .card--back { top: 631px; background: var(--back-blue); }

  .brand-block {
    position: absolute; left: 40px; width: 495px; top: 250px;
    display: flex; flex-direction: column; align-items: center; gap: 22px;
  }
  .brand-block__square {
    width: 72px; height: 72px; background: var(--brand-blue);
  }
  .brand-name {
    font-family: "Exo 2", sans-serif; font-weight: 700;
    color: var(--brand-blue); font-size: 34px; letter-spacing: 1px;
    text-transform: uppercase; white-space: nowrap;
  }

  .divider {
    position: absolute; left: 425px; top: 124px; width: 1px; height: 191px;
    background: var(--divider);
  }

  .contact { position: absolute; left: 463px; top: 128px; }
  .contact__name {
    font-family: "Exo 2", sans-serif; font-weight: 700; font-size: 31px;
    color: var(--brand-blue); text-transform: uppercase; letter-spacing: 0.5px; line-height: 1;
  }
  .contact__role {
    font-family: "Roboto", sans-serif; font-weight: 700; font-size: 20px;
    color: var(--text-gray); margin-top: 8px;
  }
  .contact__list { list-style: none; margin-top: 25px; }
  .contact__item {
    display: flex; align-items: center; gap: 12px;
    font-family: "Roboto", sans-serif; font-size: 19px; color: var(--text-gray);
    height: 26.5px;
  }
  .contact__icon { width: 18px; height: 18px; flex: none; fill: var(--brand-blue); }

  .tagline-band { position: absolute; left: 0; top: 407px; width: 825px; height: 39px; display: flex; }
  .tagline-band__blue {
    width: 622px; height: 100%; background: var(--brand-blue);
    display: flex; align-items: center; justify-content: center; padding-left: 20px;
    font-family: "Roboto", sans-serif; font-size: 19px; color: #e9f2fa; letter-spacing: 0.3px;
  }
  .tagline-band__gray { flex: 1; background: var(--brand-gray); }

  .back-name {
    position: absolute; right: 46px; bottom: 70px;
    font-family: "Exo 2", sans-serif; font-weight: 700; font-size: 44px;
    color: #ffffff; text-transform: uppercase; letter-spacing: 1px; white-space: nowrap;
  }
</style>
</head>
<body>
<main class="canvas">
  <section class="card card--front" aria-label="Business card front">
    <div class="brand-block">
      <span class="brand-block__square"></span>
      <span class="brand-name">Varneck Bidding</span>
    </div>

    <div class="divider"></div>

    <div class="contact">
      <h1 class="contact__name">Reid Halvorsen</h1>
      <p class="contact__role">Owner/President - Auctioneer</p>
      <ul class="contact__list">
        <li class="contact__item">
          <svg class="contact__icon" viewBox="0 0 24 24" aria-hidden="true"><path d="M6.6 10.8a15.1 15.1 0 0 0 6.6 6.6l2.2-2.2c.3-.3.7-.4 1-.2 1.1.4 2.3.6 3.6.6.6 0 1 .4 1 1V20c0 .6-.4 1-1 1A17 17 0 0 1 3 4c0-.6.4-1 1-1h3.5c.6 0 1 .4 1 1 0 1.3.2 2.5.6 3.6.1.3 0 .7-.2 1z"/></svg>
          702-555-0148
        </li>
        <li class="contact__item">
          <svg class="contact__icon" viewBox="0 0 24 24" aria-hidden="true"><path d="M3 6h18v12H3z M3 6l9 7 9-7" fill="none" stroke="#2f7fc4" stroke-width="2"/></svg>
          varneckbidding@postbox.net
        </li>
        <li class="contact__item">
          <svg class="contact__icon" viewBox="0 0 24 24" aria-hidden="true"><circle cx="12" cy="12" r="10"/><path d="M7 8c2 0 3 1 3 3s2 2 2 4-1 3-1 4M14 4c0 2 2 2 3 4s3 1 4 2" fill="none" stroke="#ffffff" stroke-width="1.6"/></svg>
          www.bidrevive.net
        </li>
      </ul>
    </div>

    <div class="tagline-band">
      <div class="tagline-band__blue">Improving Charity Auctions Nationwide</div>
      <div class="tagline-band__gray"></div>
    </div>
  </section>

  <section class="card card--back" aria-label="Business card back">
    <span class="back-name">Varneck Bidding</span>
  </section>
</main>
</body>
</html>
```